Corrow Family Farm fresh honey jar label

I need a label for jars of honey harvested at our farm. These are for gifts and personal use. We are looking to incorporate our farm brand into the label. We would like the design to take the existing brand and add some element like bees, honey, flowers, or hives to indicate the contents. We want the design to feel homemade and authentic without feeling cheap or hoaky

Requirements
Must have
• The label must be made to fit a 1" x2" rectangular label. The label must include the attached family brand. The label must include the text "Corrow Family Farms" "Pinebrook, USA" "Farm Fresh Honey". The label will be printed on off-white paper
Nice to have
• It would be nice to have illustrations of bees or flowers around the logo or hives or honeycombs. The label should have a vintage feel
Should not have
• The label should not feel overly cartoonish or hoaky

```html
<!DOCTYPE html>
<html lang="en">
<head>
<meta charset="utf-8">
<title>Corrow Family Farms – Farm Fresh Honey Label</title>
<link rel="stylesheet" href="https://fonts.googleapis.com/css2?family=Bebas+Neue&family=Courier+Prime:wght@700&family=Montserrat:wght@400&family=Mrs+Saint+Delafield&display=swap">
<style>
  :root {
    --page: #ffffff;
    --label: #f0dac8;
    --ink: #4a2a12;
  }
  * { margin: 0; padding: 0; box-sizing: border-box; }
  html, body { width: 1200px; height: 1200px; overflow: hidden; background: var(--page); }
  .canvas { position: relative; width: 1200px; height: 1200px; }
  .label {
    position: absolute; left: 90px; top: 329px; width: 1040px; height: 520px;
    background: var(--label);
    box-shadow: 0 1px 6px rgba(0,0,0,0.12);
    color: var(--ink);
  }
  .floral-illustration {
    position: absolute; left: 13px; top: 12px; width: 270px; height: 500px;
    background: radial-gradient(ellipse at 35% 60%, rgba(74,42,18,0.45), rgba(74,42,18,0.15) 60%, rgba(74,42,18,0) 80%);
  }
  .brand-name {
    position: absolute; left: 0; width: 1040px; top: 34px;
    text-align: center;
    font-family: "Courier Prime", monospace; font-weight: 700;
    font-size: 26px; letter-spacing: 1px;
  }
  .headline {
    position: absolute; left: 270px; top: 140px; width: 600px;
    text-align: center;
    font-family: "Bebas Neue", sans-serif;
    font-size: 128px; line-height: 1; letter-spacing: 3px;
  }
  .headline-script {
    position: absolute; left: 300px; top: 255px; width: 480px;
    text-align: center;
    font-family: "Mrs Saint Delafield", cursive;
    font-size: 170px; line-height: 1;
  }
  .farm-name {
    position: absolute; left: 360px; top: 437px; width: 380px;
    text-align: center;
    font-family: "Courier Prime", monospace; font-weight: 700;
    font-size: 25px;
  }
  .farm-location {
    position: absolute; left: 360px; top: 473px; width: 380px;
    text-align: center;
    font-family: "Montserrat", sans-serif;
    font-size: 14px; letter-spacing: 3px;
  }
</style>
</head>
<body>
<div class="canvas">
  <div class="label">
    <div class="floral-illustration" role="img" aria-label="Engraved-style illustration of wildflowers with a bumblebee hovering above"></div>
    <div class="brand-name">Corrow</div>
    <div class="headline">Farm Fresh</div>
    <div class="headline-script">Honey</div>
    <div class="farm-name">Corrow Family Farms</div>
    <div class="farm-location">Pinebrook, USA</div>
  </div>
</div>
</body>
</html>
```